Modern Business Card

Modern professional business card with more than just logo and demographic info. Something memorable.

We are a trendy/modern chiropractic group with an emphasis on neurology, hence the minimalist-type brain logo. We want to convey that modern and technical aspect with professionalism and the elite nature of our practice environment.

```html
<!DOCTYPE html>
<html lang="en">
<head>
<meta charset="utf-8">
<title>Vantage Spine Studio – Business Card</title>
<link href="https://fonts.googleapis.com/css2?family=Open+Sans:wght@400;600;700&display=swap" rel="stylesheet">
<style>
  :root {
    --brand-blue: #3d78c0;
    --brand-blue-light: #5089cf;
    --brand-blue-deep: #366db3;
    --ink: #1f1f22;
    --ink-muted: #5a5a5e;
    --card-white: #f4f4f5;
    --card-shade: #e4e4e6;
    --band-dark: #2b2b2e;
    --stage: #d9dadc;
  }
  * { box-sizing: border-box; margin: 0; padding: 0; }
  html, body {
    width: 1200px; height: 1021px; overflow: hidden;
    background: var(--stage);
    font-family: "Open Sans", Arial, sans-serif;
  }
  .stage { position: relative; width: 1200px; height: 1021px; }
  .card {
    position: absolute; left: 220px; width: 760px; height: 434px;
    box-shadow: 0 10px 28px rgba(0,0,0,.22);
    overflow: hidden;
  }

  /* Back side */
  .card-back { top: 48px; background: var(--brand-blue); }
  .card-back .pattern-field {
    position: absolute; inset: 0;
    background:
      radial-gradient(ellipse at 70% 35%, rgba(255,255,255,.10), transparent 60%),
      linear-gradient(160deg, var(--brand-blue-light), var(--brand-blue) 55%, var(--brand-blue-deep));
  }
  .card-back .wordmark {
    position: absolute; left: 64px; bottom: 78px;
    color: #ffffff;
  }

  /* Wordmark */
  .wordmark {
    display: flex; align-items: center; gap: 14px;
    font-weight: 600; font-size: 32px; letter-spacing: 1px;
    line-height: 1.05;
  }
  .wordmark .mark-square { width: 36px; height: 36px; background: currentColor; flex: none; }

  /* Front side */
  .card-front {
    top: 534px;
    background: linear-gradient(160deg, var(--card-white) 40%, var(--card-shade));
  }
  .card-front .wordmark { position: absolute; left: 58px; top: 140px; color: var(--ink); }
  .card-front .wordmark .mark-square { background: var(--brand-blue); }
  .divider {
    position: absolute; left: 398px; top: 74px; width: 2px; height: 254px;
    background: var(--ink-muted);
  }
  .divider::before {
    content: ""; position: absolute; left: 0; top: 0; width: 2px; height: 62px;
    background: var(--brand-blue);
  }
  .contact {
    position: absolute; left: 432px; top: 70px;
    color: var(--ink); font-size: 20px; line-height: 1.32;
  }
  .contact .name { color: var(--brand-blue); font-weight: 700; font-size: 25px; line-height: 1.2; }
  .contact .role { font-size: 19px; margin-bottom: 14px; }
  .contact .address { margin-bottom: 4px; }
  .contact .line { display: flex; align-items: center; gap: 8px; }
  .contact .line svg { width: 17px; height: 17px; flex: none; }
  .base-band { position: absolute; left: 0; bottom: 0; height: 18px; width: 100%; display: flex; }
  .base-band .band-blue { width: 52%; background: var(--brand-blue); }
  .base-band .band-dark { flex: 1; background: var(--band-dark); }
</style>
</head>
<body>
<main class="stage">
  <section class="card card-back">
    <div class="pattern-field" role="img" aria-label="Repeating tonal pattern of the brand symbol in lighter blue, tiled diagonally across the whole card back"></div>
    <div class="wordmark"><span class="mark-square"></span><span>VANTAGE<br>SPINE STUDIO</span></div>
  </section>

  <section class="card card-front">
    <div class="wordmark"><span class="mark-square"></span><span>VANTAGE<br>SPINE STUDIO</span></div>
    <div class="divider"></div>
    <div class="contact">
      <p class="name">Dr. Owen Lindqvist</p>
      <p class="role">President</p>
      <p class="address">4720 Maple Ridge Avenue<br>Dayton, Ohio 45402</p>
      <p class="line">
        <svg viewBox="0 0 16 16" aria-hidden="true"><path fill="#3d78c0" d="M3.6 1.5l2.3 2.6-1.3 1.8c.9 2 2.6 3.7 4.6 4.6l1.8-1.3 2.6 2.3-1.4 2.4C7 13.6 2.4 9 1.2 2.9z"/></svg>
        555-214-7730
      </p>
      <p class="line">
        <svg viewBox="0 0 16 16" aria-hidden="true"><rect x="1.5" y="3.5" width="13" height="9" fill="none" stroke="#3d78c0" stroke-width="1.6"/><path d="M1.5 3.5l6.5 5 6.5-5" fill="none" stroke="#3d78c0" stroke-width="1.6"/></svg>
        owen@vantagespine.com
      </p>
      <p class="line">
        <svg viewBox="0 0 16 16" aria-hidden="true"><g fill="none" stroke="#3d78c0" stroke-width="1.3"><circle cx="8" cy="8" r="6.5"/><ellipse cx="8" cy="8" rx="3" ry="6.5"/><path d="M1.5 8h13M2.5 5h11M2.5 11h11"/></g></svg>
        www.vantagespine.com
      </p>
    </div>
    <div class="base-band"><span class="band-blue"></span><span class="band-dark"></span></div>
  </section>
</main>
</body>
</html>
```